Professional looking Roller Blind Discount Card that portrays quality at a value for money price!

We need a double sided business card designed as a discount card. Size 90mm wide x 55mm high.We would like it to look professional and portray quality at a value for money price point.I have uploaded a word document with a basic layout with the information we want included on each side of the card. Please put your own thought into the layout.

Contact Information for Business Card

As per word document attached.

```html
<!DOCTYPE html>
<html lang="en">
<head>
<meta charset="utf-8">
<title>Roller Blinds Discount Card</title>
<link href="https://fonts.googleapis.com/css2?family=Poppins:wght@400;500;600;700&family=Oswald:wght@600&family=Playball&display=swap" rel="stylesheet">
<style>
  :root {
    --blue: #27a6e1;
    --blue-deep: #1a7fd6;
    --blue-light: #5cc4f0;
    --ink: #4a4a4a;
    --bar-grey: #5f5f5f;
    --bg: #eeeeee;
    --card: #ffffff;
  }
  * { margin: 0; padding: 0; box-sizing: border-box; }
  html, body { width: 1125px; height: 1200px; overflow: hidden; background: var(--bg); }
  .stage {
    position: absolute; left: 0; top: 0;
    width: 1090px; height: 1163px;
    transform: scale(1.0321); transform-origin: 0 0;
  }
  .card {
    position: absolute; left: 166px; width: 800px; height: 457px;
    background: var(--card);
    font-family: 'Poppins', sans-serif; color: var(--ink);
  }
  .card--front { top: 103px; }
  .card--back { top: 620px; }
  .card__bar { position: absolute; left: 0; bottom: 0; width: 800px; height: 10px; }

  /* front */
  .headline {
    position: absolute; left: 0; top: 22px; width: 800px; text-align: center;
    font-weight: 600; font-size: 100px; line-height: 1; color: var(--blue); letter-spacing: 1px;
  }
  .headline__rule { position: absolute; top: 68px; width: 98px; height: 18px; }
  .headline__rule--left { left: 86px; }
  .headline__rule--right { left: 614px; }
  .subline {
    position: absolute; left: 0; width: 800px; text-align: center;
    font-size: 35px; line-height: 1; font-weight: 400;
  }
  .subline--one { top: 112px; }
  .subline--two { top: 149px; }
  .badge { position: absolute; top: 204px; width: 180px; height: 180px; }
  .badge svg { position: absolute; inset: 0; }
  .badge__text {
    position: absolute; inset: 0; display: flex; align-items: center; justify-content: center;
    text-align: center; font-family: 'Oswald', sans-serif; font-weight: 600;
    color: #fff; font-size: 23px; line-height: 1.15; text-shadow: 0 1px 2px rgba(0,40,90,.45);
  }
  .badge--one { left: 102px; }
  .badge--two { left: 297px; }
  .badge--three { left: 486px; }
  .call {
    position: absolute; left: 0; width: 800px; text-align: center;
    font-size: 34px; line-height: 1; font-weight: 400;
  }
  .call strong { color: var(--blue); font-weight: 600; }
  .call--front { top: 398px; }

  /* back */
  .title {
    position: absolute; left: 28px; top: 20px;
    font-weight: 700; font-size: 94px; line-height: 1; color: var(--blue); letter-spacing: 1px;
  }
  .tagline {
    position: absolute; left: 31px; top: 106px;
    font-size: 44px; line-height: 1; font-weight: 400;
  }
  .tagline strong { font-weight: 600; }
  .photo {
    position: absolute; left: 32px; top: 162px; width: 490px; height: 263px;
    background: linear-gradient(90deg, #6e5a4d 0%, #6b5b4c 30%, #4f6b3e 34%, #7d9a5c 60%, #a9b59a 80%, #d2d0c8 100%);
  }
  .call-strip {
    position: absolute; left: 32px; top: 370px; width: 490px; height: 55px;
    background: var(--blue); color: #fff;
    display: flex; align-items: center; justify-content: center;
    font-size: 33px; font-weight: 400;
  }
  .call-strip strong { font-weight: 600; }
  .bubble { position: absolute; left: 558px; top: 172px; width: 200px; height: 130px; }
  .bubble__text {
    position: absolute; left: 8px; top: 18px; width: 184px; text-align: center;
    font-family: 'Playball', cursive; color: #fff; font-size: 24px; line-height: 1.05;
    text-shadow: 0 1px 2px rgba(0,40,90,.4);
  }
  .brand {
    position: absolute; left: 532px; top: 392px; display: flex; align-items: center; gap: 10px;
    font-family: 'Poppins', sans-serif; font-weight: 500; font-size: 24px; color: var(--blue);
  }
  .brand__mark { width: 18px; height: 18px; background: var(--blue); }
</style>
</head>
<body>
<div class="stage">

  <section class="card card--front">
    <svg class="headline__rule headline__rule--left" viewBox="0 0 98 18"><g fill="#27a6e1"><rect y="0" width="98" height="3"/><rect y="7" width="98" height="3"/><rect y="14" width="98" height="3"/></g></svg>
    <h1 class="headline">25% OFF</h1>
    <svg class="headline__rule headline__rule--right" viewBox="0 0 98 18"><g fill="#27a6e1"><rect y="0" width="98" height="3"/><rect y="7" width="98" height="3"/><rect y="14" width="98" height="3"/></g></svg>
    <p class="subline subline--one">Quality Custom Made Roller Blinds</p>
    <p class="subline subline--two">Blockout - screen - LightFiltering</p>

    <svg width="0" height="0" style="position:absolute">
      <defs>
        <linearGradient id="badgeFill" x1="0" y1="0" x2="0" y2="1">
          <stop offset="0" stop-color="#7fd3f6"/>
          <stop offset="0.5" stop-color="#2ea3e6"/>
          <stop offset="1" stop-color="#1a78d8"/>
        </linearGradient>
      </defs>
    </svg>

    <div class="badge badge--one">
      <svg viewBox="0 0 180 180"><circle cx="90" cy="90" r="82" fill="none" stroke="#2a9be3" stroke-width="12" stroke-dasharray="4.3 4.3"/><circle cx="90" cy="90" r="79" fill="#2a9be3"/><circle cx="90" cy="90" r="74" fill="none" stroke="#fff" stroke-width="3"/><circle cx="90" cy="90" r="71" fill="url(#badgeFill)"/></svg>
      <div class="badge__text">FREE<br>in Home<br>Measure &amp;<br>Quote</div>
    </div>
    <div class="badge badge--two">
      <svg viewBox="0 0 180 180"><circle cx="90" cy="90" r="82" fill="none" stroke="#2a9be3" stroke-width="12" stroke-dasharray="4.3 4.3"/><circle cx="90" cy="90" r="79" fill="#2a9be3"/><circle cx="90" cy="90" r="74" fill="none" stroke="#fff" stroke-width="3"/><circle cx="90" cy="90" r="71" fill="url(#badgeFill)"/></svg>
      <div class="badge__text">Best Price<br>Guarantee</div>
    </div>
    <div class="badge badge--three">
      <svg viewBox="0 0 180 180"><circle cx="90" cy="90" r="82" fill="none" stroke="#2a9be3" stroke-width="12" stroke-dasharray="4.3 4.3"/><circle cx="90" cy="90" r="79" fill="#2a9be3"/><circle cx="90" cy="90" r="74" fill="none" stroke="#fff" stroke-width="3"/><circle cx="90" cy="90" r="71" fill="url(#badgeFill)"/></svg>
      <div class="badge__text">Family<br>Owned &amp;<br>Operated</div>
    </div>

    <p class="call call--front">CALL <strong>0400 275 319</strong> TODAY!</p>
    <svg class="card__bar" viewBox="0 0 800 10" preserveAspectRatio="none"><polygon points="0,0 435,0 425,10 0,10" fill="#27a6e1"/><polygon points="435,0 800,0 800,10 425,10" fill="#5f5f5f"/></svg>
  </section>

  <section class="card card--back">
    <h2 class="title">ROLLER BLINDS</h2>
    <p class="tagline"><strong>FREE</strong> in Home Meacure &amp; Quote</p>
    <div class="photo" role="img" aria-label="Photo of a room with large windows looking out onto a leafy garden"></div>
    <p class="call-strip">CALL&nbsp;<strong>0400 275 319</strong>&nbsp;TODAY!</p>

    <div class="bubble">
      <svg viewBox="0 0 200 130" width="200" height="130">
        <defs>
          <linearGradient id="bubbleFill" x1="0" y1="0" x2="0" y2="1">
            <stop offset="0" stop-color="#8fdaf8"/>
            <stop offset="0.45" stop-color="#2ea6ea"/>
            <stop offset="1" stop-color="#1b74d6"/>
          </linearGradient>
        </defs>
        <path d="M100 4 C152 4 196 26 196 58 C196 90 152 110 100 110 C86 110 74 109 62 106 L36 128 L42 100 C16 90 4 76 4 58 C4 26 48 4 100 4 Z" fill="url(#bubbleFill)" stroke="#1f8fe0" stroke-width="2"/>
      </svg>
      <div class="bubble__text">Huge Selection<br>of Fabrics</div>
    </div>

    <div class="brand"><span class="brand__mark"></span>B&amp;K INTERIORS</div>
    <svg class="card__bar" viewBox="0 0 800 10" preserveAspectRatio="none"><polygon points="0,0 435,0 425,10 0,10" fill="#27a6e1"/><polygon points="435,0 800,0 800,10 425,10" fill="#5f5f5f"/></svg>
  </section>

</div>
</body>
</html>
```